Landing Page Design

This project needs landing page desing only. However, whoever wins this round will get to work directly on all other pages of the website as a separate private project.

See attached file for more details.

Target Market(s)

25-60 year old person who is looking for health insurance quotes.

Industry/Entity Type

Health Insurance

Number of Pages Required

1 page

Font styles to use
Sans Serif

Requirements
Must have
• see attachment
Nice to have
• see attachment
Should not have
• see attachment

```html
<!DOCTYPE html>
<html lang="en">
<head>
<meta charset="utf-8">
<title>CoverCompass.com – Compare Health Insurance Plans</title>
<link rel="stylesheet" href="https://fonts.googleapis.com/css2?family=Lato:wght@300;400;700;900&display=swap">
<style>
:root{
  --blue:#1680b8;
  --blue-dark:#10679a;
  --orange:#f07c22;
  --red:#c63a2b;
  --ink:#333;
  --muted:#777;
  --line:#e3e3e3;
  --dark:#262626;
  --black:#111;
}
*{box-sizing:border-box;margin:0;padding:0}
html,body{width:742px;height:1200px;overflow:hidden;background:#fff}
body{font-family:'Lato',sans-serif;color:var(--ink);position:relative}
.abs{position:absolute}

/* top bar */
.topbar{left:0;top:0;width:742px;height:30px;background:var(--blue)}
.brand{font-weight:700;color:#fff;font-size:13px;display:flex;align-items:center;gap:5px}
.brand .dot{width:10px;height:10px;background:#fff;border-radius:2px}
.topbar .brand{left:128px;top:7px}
.call-tab{right:0;top:0;width:130px;height:30px;background:var(--red);clip-path:polygon(12px 0,100% 0,100% 100%,0 100%);color:#fff;text-align:center;padding-left:8px}
.call-tab small{display:block;font-size:5.5px;margin-top:6px;letter-spacing:.3px}
.call-tab b{font-size:9px}

/* hero */
.hero{left:0;top:30px;width:742px;height:203px;overflow:hidden}
.hero-photo{position:absolute;inset:0;background:linear-gradient(100deg,#6b4a36 0%,#b88764 30%,#e6c2a2 55%,#d7c8bb 80%,#c9c3bd 100%)}
.hero-shade{position:absolute;inset:0;background:linear-gradient(90deg,rgba(0,0,0,.25),rgba(0,0,0,0) 60%)}
.hero-title{position:absolute;left:156px;top:62px;color:#fff;line-height:1.05}
.hero-title .light{font-weight:300;font-size:17px}
.hero-title .bold{font-weight:900;font-size:22px;display:block}
.chevron{position:absolute;left:128px;top:92px}
.quote-circle{position:absolute;left:410px;top:18px;width:144px;height:144px;border-radius:50%;background:rgba(255,255,255,.93);text-align:center;color:var(--blue);border:3px solid rgba(255,255,255,.6)}
.quote-circle p{font-size:15px;font-weight:300;line-height:1.25}
.quote-circle .free{font-weight:900;font-size:16px}
.quote-circle .head{margin-top:14px}
.zip{display:block;margin:8px auto 0;width:84px;height:19px;border:1px solid var(--orange);background:#fff;color:var(--orange);font-size:6.5px;line-height:17px}
.btn{background:var(--orange);color:#fff;font-size:6.5px;text-align:center}
.quote-circle .btn{display:block;margin:8px auto 0;width:62px;height:19px;line-height:19px}
.partners{position:absolute;left:386px;top:175px;display:flex;gap:2px}
.partners span{width:45px;height:21px;background:#f2f2f2;border:1px solid #fff}

/* phone band */
.phone-band{left:0;top:233px;width:742px;height:51px;background:var(--blue);color:#fff;text-align:center}
.phone-band h2{font-weight:400;font-size:15px;margin-top:8px}
.phone-band h2 .num{background:var(--red);font-weight:700;padding:0 4px}
.phone-band p{font-style:italic;font-weight:300;font-size:8px;margin-top:4px}

/* section heading */
.sec-title{left:0;width:742px;text-align:center;font-size:11px;font-weight:700;color:#222}
.sec-title::after{content:"";display:block;width:60px;height:1px;margin:5px auto 0;background:linear-gradient(90deg,var(--orange),var(--blue))}

/* faq grid */
.faq{width:237px;height:60px;border-bottom:1px solid var(--line);display:flex;gap:7px}
.faq.active{border-bottom-color:var(--blue)}
.faq .icon{flex:0 0 42px;height:50px;border:1px solid var(--line);display:flex;align-items:center;justify-content:center}
.faq.active .icon{border-color:var(--blue)}
.faq h3{font-size:5.6px;font-weight:400;color:var(--blue);text-transform:uppercase;margin-bottom:3px}
.faq p{font-size:5.2px;line-height:1.65;color:var(--muted)}
.faq a{font-size:5.2px;color:var(--blue);text-decoration:none;display:block;margin-top:3px}
.faq.active a{color:var(--muted)}

/* testimonials */
.testimonials{left:0;top:578px;width:742px;height:143px;background:linear-gradient(180deg,#2a2622,#1d1a18);}
.card{position:absolute;top:27px;width:152px;height:50px;background:#fff;border-radius:3px;padding:8px 14px 0;font-size:5.2px;line-height:1.45;color:#777;text-align:center}
.card::before{content:"\201D";position:absolute;left:7px;top:1px;font-size:10px;color:#999}
.card::after{content:"";position:absolute;left:36px;bottom:-5px;border:5px solid transparent;border-bottom:0;border-top-color:#fff}
.person{position:absolute;top:84px;display:flex;align-items:center;gap:7px;color:#ddd;font-size:5.8px;line-height:1.6}
.avatar{width:32px;height:32px;border-radius:50%;background:linear-gradient(135deg,#8a6a58,#4a3a32);border:2px solid #fff}
.person .co{color:var(--blue);margin-left:6px}

/* plan tables */
.plan{width:236px}
.plan .badge{position:absolute;left:0;top:0;width:63px;height:63px;border-radius:50%;background:var(--blue);border:2px solid #fff;box-shadow:0 0 0 1px var(--blue);color:#fff;text-align:center;font-size:10px;line-height:1.2;display:flex;align-items:center;justify-content:center;z-index:1}
.plan table{position:absolute;left:0;top:33px;width:236px;border-collapse:collapse;font-size:5.8px;text-align:center}
.plan th{height:34px;color:var(--blue);font-weight:400;border:1px solid var(--line);border-bottom:0}
.plan th.lab{border:0;background:var(--blue)}
.plan td{height:27px;border:1px solid var(--line);color:#444}
.plan td.lab{width:63px;background:var(--blue);color:#fff;font-size:4.8px;font-weight:700;text-transform:uppercase;border-color:#4d9bc8;line-height:1.2}

/* cta band */
.cta{left:0;top:984px;width:742px;height:77px;background:linear-gradient(90deg,#2b2b2b,#1f1f1f)}
.cta h2{position:absolute;left:128px;top:16px;color:#fff;font-size:13px;font-weight:700}
.cta .zip{position:absolute;left:129px;top:38px;margin:0;width:64px;height:20px;line-height:18px}
.cta .btn{position:absolute;left:200px;top:38px;width:61px;height:20px;line-height:20px}
.cta .slash{position:absolute;left:370px;top:0}
.agent{position:absolute;left:420px;top:17px;width:152px;text-align:center;color:#fff}
.agent h3{font-size:10px;font-weight:700}
.agent .num{display:block;margin:6px auto 0;width:104px;height:20px;line-height:20px;background:var(--red);font-size:11px;font-weight:700}
.agent p{font-size:7px;font-weight:700;margin-top:4px}

/* footer */
.footer{left:0;top:1061px;width:742px;height:139px;background:var(--black);color:#888}
.footer .brand{position:absolute;left:128px;top:20px}
.addr{position:absolute;left:129px;top:44px;font-size:5.8px;line-height:1.55;color:#bbb}
.links{position:absolute;top:19px;list-style:none;font-size:6px;line-height:1.85;color:#777}
.links .on{color:var(--red)}
.footer .callnow{position:absolute;left:489px;top:17px;font-size:7.5px;color:#ddd;line-height:1.4}
.footer .callnow b{color:#fff}
.seal{position:absolute;top:50px;height:23px;border-radius:3px}
.divider{position:absolute;left:128px;top:89px;width:486px;height:1px;background:#2c2c2c}
.legal{position:absolute;left:0;top:99px;width:742px;text-align:center;font-size:5.2px;line-height:1.75;color:#666}
</style>
</head>
<body>

<header class="abs topbar">
  <div class="abs brand"><span class="dot"></span>CoverCompass.com</div>
  <div class="abs call-tab"><small>CALL AN AGENT</small><b>1-800-555-0142</b></div>
</header>

<section class="abs hero">
  <div class="hero-photo" role="img" aria-label="Smiling family of three close together in a warm, bright home"></div>
  <div class="hero-shade"></div>
  <svg class="chevron" width="10" height="18" viewBox="0 0 10 18"><path d="M8 2 2 9l6 7" fill="none" stroke="#fff" stroke-width="1.3"/></svg>
  <h1 class="hero-title">
    <span class="light">COMPARE 2016</span>
    <span class="bold">HEALTH</span>
    <span class="bold">INSURANCE</span>
    <span class="light">PLANS</span>
  </h1>
  <div class="quote-circle">
    <p class="head">Get Your</p>
    <p class="free">FREE</p>
    <p>Quotes Now!</p>
    <span class="zip">Enter Zip Code</span>
    <span class="btn">See Plans</span>
  </div>
  <div class="partners" aria-label="Partner carriers"><span></span><span></span><span></span><span></span></div>
</section>

<section class="abs phone-band">
  <h2>To shop over the phone call <span class="num">1-800-555-0142</span></h2>
  <p>Speak with a licensed agent and get expert advice on choosing a plan that's right for you</p>
</section>

<h2 class="abs sec-title" style="top:308px">How do I Buy Health Insurance?</h2>

<article class="abs faq active" style="left:128px;top:342px">
  <div class="icon"><svg width="26" height="26" viewBox="0 0 26 26" fill="none" stroke="#1680b8" stroke-width="1.2"><circle cx="8" cy="6" r="2.5"/><circle cx="18" cy="6" r="2.5"/><path d="M5 24V11h6v13M15 24V11h6v13"/></svg></div>
  <div><h3>How do I buy health insurance?</h3><p>For some, buying health insurance can be a confusing and overwhelming process. First, you have to find a health insurance plan within your budget. Then you have to contact the company...</p><a>Learn more...</a></div>
</article>
<article class="abs faq" style="left:378px;top:342px">
  <div class="icon"><svg width="26" height="24" viewBox="0 0 26 24" fill="none" stroke="#999" stroke-width="1.2"><path d="M13 22 3 12a5.5 5.5 0 0 1 10-7 5.5 5.5 0 0 1 10 7z"/><path d="M4 12h5l2-4 3 7 2-3h6"/></svg></div>
  <div><h3>What is the healthcare marketplace?</h3><p>The passage of the Affordable Care Act established the Healthcare Marketplace. There are two distinct divisions - a state level, and a federal level. 37 states are members of the federal exchange...</p><a>Learn more...</a></div>
</article>
<article class="abs faq" style="left:128px;top:416px">
  <div class="icon"><svg width="28" height="22" viewBox="0 0 28 22" fill="none" stroke="#999" stroke-width="1.2"><rect x="5" y="5" width="18" height="12" rx="1"/><circle cx="14" cy="11" r="3"/><path d="M2 8 5 5 2 2M26 14l-3 3 3 3"/></svg></div>
  <div><h3>What's the "health insurance exchange"?</h3><p>The Health Insurance Exchange is the pool of health care plans and providers which are cooperating with the federal government in order to provide affordable health insurance...</p><a>Learn more...</a></div>
</article>
<article class="abs faq" style="left:378px;top:416px">
  <div class="icon"><svg width="26" height="26" viewBox="0 0 26 26" fill="none" stroke="#999" stroke-width="1.2"><circle cx="13" cy="13" r="11"/><circle cx="13" cy="14" r="5"/><path d="M13 14l2-2M12 6h2"/></svg></div>
  <div><h3>When can I sign up for health insurance?</h3><p>Obamacare - a nickname (sometimes considered derogatory) for the Affordable Care Act. Its full name is the Patient Protection and Affordable Care Act. It was signed into law by President...</p><a>Learn more...</a></div>
</article>
<article class="abs faq" style="left:128px;top:492px">
  <div class="icon"><svg width="26" height="26" viewBox="0 0 26 26" fill="none" stroke="#999" stroke-width="1.2"><rect x="3" y="3" width="14" height="19" rx="1"/><path d="M6 8h8M6 12h8M6 16h5"/><path d="M19 11l5 2v4c0 3-2 5-5 6-3-1-5-3-5-6v-4z" fill="#fff"/><path d="M17 17l2 2 3-4"/></svg></div>
  <div><h3>How can I find the best health insurance company?</h3><p>Right now, there are hundreds of different health insurance companies participating in the Exchange offering thousands of different plans. These companies are rated on a letter grading scale...</p><a>Learn more...</a></div>
</article>
<article class="abs faq" style="left:378px;top:492px">
  <div class="icon"><svg width="26" height="26" viewBox="0 0 26 26" fill="none" stroke="#999" stroke-width="1.2"><circle cx="13" cy="13" r="11"/><path d="M13 8v10M8 13h10"/></svg></div>
  <div><h3>What happens if I still can't afford</h3><p>If you cannot purchase insurance, the government will charge you a fine when you file your yearly income taxes. For 2015, the fine will be either $325 or 2% of your income...</p><a>Learn more...</a></div>
</article>

<section class="abs testimonials" role="img" aria-label="Dark mosaic of customer portraits behind the testimonials">
  <div class="card" style="left:129px">Switching plans took one short call, and the agent explained every option clearly so we could choose with confidence.</div>
  <div class="card" style="left:294px">I compared four plans side by side in minutes and found better coverage for my family at a lower monthly price.</div>
  <div class="card" style="left:461px">Friendly, patient advice from start to finish. I finally understand my deductible and what my plan really covers.</div>
  <div class="person" style="left:131px"><div class="avatar" role="img" aria-label="Customer portrait"></div><div>Daniel Reyes<br>Executive Director<span class="co">Company Inc.</span></div></div>
  <div class="person" style="left:297px"><div class="avatar" role="img" aria-label="Customer portrait"></div><div>Daniel Reyes<br>Executive Director<span class="co">Company Inc.</span></div></div>
  <div class="person" style="left:463px"><div class="avatar" role="img" aria-label="Customer portrait"></div><div>Daniel Reyes<br>Executive Director<span class="co">Company Inc.</span></div></div>
</section>

<h2 class="abs sec-title" style="top:745px">Health Insurance Plan Types</h2>

<div class="abs plan" style="left:129px;top:782px">
  <div class="badge">PLAN<br>TYPES</div>
  <table>
    <tr><th class="lab"></th><th>PPO</th><th>EPO</th><th>POS</th><th>HMO</th></tr>
    <tr><td class="lab">PCP<br>Required?</td><td>No</td><td>No</td><td>Yes</td><td>Yes</td></tr>
    <tr><td class="lab">Referrals<br>Required?</td><td>No</td><td>No</td><td>Yes</td><td>Yes</td></tr>
    <tr><td class="lab">Pre<br>Authorization<br>Required?</td><td>Yes</td><td>Yes</td><td>No</td><td>No</td></tr>
    <tr><td class="lab">Out-of-network<br>Coverage?</td><td>Yes</td><td>Yes</td><td>No</td><td>No</td></tr>
  </table>
</div>

<div class="abs plan" style="left:378px;top:782px">
  <div class="badge">TIERS</div>
  <table>
    <tr><th class="lab"></th><th>BRONZE</th><th>SLIVER</th><th>GOLD</th><th>PLATINUM</th></tr>
    <tr><td class="lab">Coverage<br>Level</td><td>60%</td><td>70%</td><td>80%</td><td>90%</td></tr>
    <tr><td class="lab">Premium<br>Level</td><td>Lowest</td><td>2nd<br>Lowest</td><td>2nd<br>Highest</td><td>Highest</td></tr>
    <tr><td class="lab">Deductible</td><td>Highest</td><td>Modetate</td><td>None</td><td>None</td></tr>
    <tr><td class="lab">Cost-sharing</td><td>None</td><td>Yes</td><td>None</td><td>None</td></tr>
  </table>
</div>

<section class="abs cta">
  <h2>Compare Health Insurance Plans Online</h2>
  <span class="zip">Enter Zip Code</span>
  <span class="btn">Get Quotes</span>
  <svg class="slash" width="40" height="77" viewBox="0 0 40 77"><path d="M38 0 2 77" stroke="#666" stroke-width=".8"/></svg>
  <div class="agent"><h3>Speak To A Licensed Agent</h3><span class="num">1-800-555-0142</span><p>Mon-Fri, 8am-8pm EST</p></div>
</section>

<footer class="abs footer">
  <div class="brand"><span class="dot"></span>CoverCompass.com</div>
  <p class="addr">120 Maple Ave,<br>Suite 300, Springfield,<br>OH 45501</p>
  <ul class="links" style="left:294px"><li class="on">Home</li><li>Partners</li><li>Insurance Basics</li><li>FAQs</li></ul>
  <ul class="links" style="left:378px"><li>About Us</li><li>Contact Us</li><li>Privacy Policy</li><li>Terms of Use</li></ul>
  <p class="callnow">Call now to get your free quote<br>comparison <b>(800) 555-0142</b></p>
  <span class="seal" style="left:493px;width:59px;background:#2f6d96"></span>
  <span class="seal" style="left:564px;width:46px;background:#d9d9d9;border-radius:10px"></span>
  <div class="divider"></div>
  <p class="legal">By using this website, I confirm that I understand and agree to the applicable Privacy Policy and Terms of Service.<br>*Not connected with or endorsed by the United States government or the federal Medicare program.<br>Copyright © 2015 CoverCompass.com. All rights reserved.</p>
</footer>

</body>
</html>
```